Marlowe's Stone Hearth Pizzeria Pitch Deck

Clean and Minimalist Layout: Use a clean and uncluttered layout with ample white space to enhance readability and focus on the key content.

Color Palette: Choose a color scheme that aligns with your brand identity. Black and White. Opt for a combination of complementary colors to create a visually appealing and cohesive look throughout the presentation.

Typography: Select modern and legible fonts for headings and body text. Consider using a combination of serif and sans-serif fonts to create contrast and hierarchy.

High-Quality Images: Incorporate high-resolution images that visually represent your pizzeria, food offerings, and brand. Ensure the images are clear, well-lit, and of professional quality.

Graphs and Charts: Utilize visually appealing graphs and charts to present financial projections, market data, and growth metrics. Choose appropriate chart types, such as bar graphs or line charts, to effectively communicate data.

Iconography: Include relevant icons and symbols to enhance visual interest and provide quick visual cues. Use them to represent different sections, services, or key points in your presentation.

Slide Transitions and Animations: Use subtle slide transitions and animations to add a touch of interactivity and engage your audience. However, avoid overusing flashy animations that may distract from the content.

Consistent Branding: Ensure that your pitch deck maintains consistent branding elements throughout, such as your logo, color scheme, and typography. This helps to reinforce your brand identity and create a cohesive presentation.

Remember, the goal is to create a visually appealing and professional pitch deck that effectively communicates your key messages. Use visuals, graphs, and design elements strategically to enhance understanding and engagement with your audience.

Target Market(s)

Investors

Industry/Entity Type

Food Industry

Font styles to use
Serif

Colors

Designer to choose only greyscale colors for use in the design.

Requirements
Must have
• Modern and Professional Look: Opt for a modern design that reflects the professional nature of your business. Use clean lines, contemporary fonts, and a visually appealing color scheme to create a polished and professional appearance. Consistent Branding: Incorporate your pizzeria's branding elements such as the logo, colors, and typography throughout the pitch deck. Consistency in branding helps to establish a cohesive and memorable visual identity. Visual Hierarchy: Use visual hierarchy to guide the viewer's attention and emphasize important information. Utilize font sizes, colors, and formatting techniques such as bold and italics to differentiate headings, subheadings, and body text. Engaging Visuals: Incorporate relevant and eye-catching visuals such as high-quality images, graphics, and icons. Visuals should support your content and help communicate your message effectively. Well-Structured Layout: Organize your content into sections and use clear headings and subheadings to create a logical flow. Ensure that each slide has enough white space for readability and avoid cluttered designs. Legible Fonts: Choose fonts that are easy to read on both computer screens and projection screens. Stick to a maximum of two font styles to maintain a clean and professional look. Charts and Graphs: When presenting data or statistics, use charts, graphs, and infographics to present information visually. This makes complex information more digestible and visually appealing. Slide Transitions and Animations: Use slide transitions and subtle animations to enhance the visual experience. However, avoid excessive animations that can distract from your content. Balance of Text and Visuals: Strike a balance between text and visuals. Avoid overcrowding slides with excessive text and focus on presenting key points in a concise and visually appealing manner. Relevance to Content: Ensure that the design elements align with and enhance the content of your pitch deck. Avoid using decorative elements that do not serve a purpose or distract from the main message. Remember, the design should complement and support your content rather than overpowering it. A well-designed pitch deck will capture attention, convey professionalism, and enhance the overall impact of your presentation.

```html
<!DOCTYPE html>
<html lang="en">
<head>
<meta charset="utf-8">
<title>Marlowe's Stone Hearth Pizzeria – Pitch Deck</title>
<link rel="stylesheet" href="https://fonts.googleapis.com/css2?family=DM+Sans:wght@400;500;600;700&family=DM+Serif+Display&display=swap">
<style>
:root{
  --white:#ffffff;
  --black:#000000;
  --ink:#1a1a1a;
  --grey:#7f7f7f;
  --grey-rule:#8a8a8a;
  --muted:#9a9a9a;
  --shadow:rgba(0,0,0,.32);
}
*{box-sizing:border-box;margin:0;padding:0}
html,body{width:1200px;height:2194px;overflow:hidden;background:var(--white)}
body{position:relative;font-family:"DM Sans",Arial,sans-serif;color:var(--ink)}
.slide{position:absolute;width:541px;height:304px;overflow:hidden;background:var(--white);box-shadow:0 10px 28px var(--shadow)}
.slide.dark{background:var(--black);color:var(--white)}
.abs{position:absolute}
.photo{position:absolute;border-radius:50%}
.heading{position:absolute;font-family:"DM Serif Display",Georgia,serif;font-weight:400;font-size:26px;line-height:1.15;color:var(--black);letter-spacing:-.2px;white-space:nowrap}
.dark .heading,.heading.light{color:var(--white)}
.rule{position:absolute;height:3px;width:50px;background:var(--grey-rule)}
.sub{position:absolute;font-weight:600;font-size:16.5px;line-height:1.55;white-space:nowrap}
.body{position:absolute;font-size:9.6px;line-height:1.52}
.body b{font-weight:700}
.body p+p{margin-top:7px}
.brand{position:absolute;font-family:"DM Serif Display",Georgia,serif;font-size:17px;color:var(--black);line-height:1;white-space:nowrap}
.brand.light{color:var(--white)}
.footer-url{position:absolute;left:41px;top:286px;font-size:6px;color:var(--muted)}
.follow{position:absolute;left:263px;top:286px;font-size:6px;color:var(--ink);display:flex;align-items:center;gap:3px}
.follow i{display:inline-block;width:4px;height:4px;border-radius:50%;background:currentColor}
.dark .follow,.follow.light{color:var(--white)}
.page{position:absolute;left:495px;top:286px;font-size:6px;color:var(--muted)}
.stroke{position:absolute;left:0;top:0;width:541px;height:304px;pointer-events:none}
/* cover */
.cover{background:var(--grey)}
.cover .band{position:absolute;left:0;width:541px;height:16px;background:linear-gradient(#3a3a3a,#1e1e1e)}
.cover .paper{position:absolute;left:0;top:77px;width:541px;height:145px;background:linear-gradient(100deg,#cfcdca,#bdbbb8 60%,#c7c5c2)}
.cover .mark{position:absolute;left:58px;top:112px;width:170px;text-align:center;font-family:"DM Serif Display",Georgia,serif;color:var(--black)}
.cover .mark .n{font-size:34px;line-height:1}
.cover .mark .t{font-size:11px;letter-spacing:2px;margin-top:6px}
.cover .contact{position:absolute;left:0;top:243px;width:541px;text-align:center;font-size:8.6px;line-height:1.32;color:var(--white)}
.cover .url{position:absolute;left:0;top:288px;width:541px;text-align:center;font-size:6px;color:var(--white)}
/* business model */
.bm-text{position:absolute;left:291px;width:230px;font-size:7.7px;line-height:1.36;color:var(--white)}
.bm-text h4{font-family:"DM Serif Display",Georgia,serif;font-weight:400;font-size:9.4px;line-height:1.2}
.icon-disc{position:absolute;border-radius:50%;border:2px solid var(--white)}
.icon-disc span{position:absolute;left:0;right:0;top:50%;transform:translateY(-50%);text-align:center;font-size:10px;color:var(--white)}
</style>
</head>
<body>

<!-- Cover -->
<section class="slide cover" style="left:34px;top:83px">
  <div class="band" style="top:61px"></div>
  <div class="paper"></div>
  <div class="band" style="top:222px;height:13px"></div>
  <div class="mark"><div class="n">Marlowe's</div><div class="t">STONE HEARTH PIZZERIA</div></div>
  <div class="photo" role="img" aria-label="Top-down photo of a pizza with rocket, prosciutto and balsamic glaze" style="left:332px;top:70px;width:160px;height:158px;background:radial-gradient(circle at 45% 45%,#6f8f3a,#4f6e2a 55%,#c9a05a 75%,#b38a48)"></div>
  <div class="contact">Contact Information:<br>Owen Castell (Owner &amp; CEO): owen@marlowesstonehearth.com<br>Priya Lenfant (Owner, Silent Partner): priya@marlowesstonehearth.com</div>
  <div class="url">www.marlowesstonehearth.com</div>
</section>

<!-- About -->
<section class="slide" style="left:613px;top:327px">
  <div class="photo" role="img" aria-label="Pizza baking in a wood-fired oven with flames behind" style="left:311px;top:-23px;width:348px;height:348px;background:radial-gradient(circle at 40% 40%,#f2b450,#c9661c 45%,#6b2a0c 80%,#3a1606)"></div>
  <svg class="stroke" viewBox="0 0 541 304"><path d="M400 10 C330 70 320 220 395 300" fill="none" stroke="#fff" stroke-width="2.5" stroke-linecap="round"/></svg>
  <h2 class="heading" style="left:45px;top:27px">About</h2>
  <div class="brand" style="left:128px;top:34px">Marlowe's</div>
  <div class="rule" style="left:45px;top:66px"></div>
  <div class="body" style="left:45px;top:80px;width:245px">
    <p>Marlowe's Stone Hearth Pizzeria is a quality casual restaurant offering freshly cooked, delicious pizzas made with carefully crafted homemade sauce and dough. We prioritize customer satisfaction and provide lightning-quick food times, making us a top choice for takeout and delivery.</p>
    <p><b>Vision and Mission Statement:</b> Our vision is to become the go-to destination for exceptional pizza experiences, known for our quality ingredients and outstanding service. Our mission is to delight customers with every bite and create memorable moments through our delicious pizzas.</p>
  </div>
  <div class="footer-url">www.marlowesstonehearth.com</div>
  <div class="follow">Follow Us <i></i><i></i></div>
</section>

<!-- Section divider -->
<section class="slide dark" style="left:34px;top:570px">
  <div class="photo" role="img" aria-label="Cheese pizza coming out of a flaming brick oven" style="left:-125px;top:-175px;width:430px;height:430px;background:radial-gradient(circle at 60% 70%,#e0802a,#b4461a 40%,#5a2a12 75%,#2a150a)"></div>
  <svg class="stroke" viewBox="0 0 541 304"><path d="M270 30 C300 110 270 210 160 258" fill="none" stroke="#fff" stroke-width="2.5" stroke-linecap="round"/></svg>
  <div class="brand light" style="left:425px;top:27px">Marlowe's</div>
  <h2 class="heading" style="left:301px;top:113px;font-size:30px;line-height:1.25">The Market<br>Opportunity</h2>
  <div class="rule" style="left:297px;top:199px"></div>
  <div class="footer-url">www.marlowesstonehearth.com</div>
  <div class="follow">Follow Us <i></i><i></i></div>
  <div class="page">- 3</div>
</section>

<!-- Industry overview -->
<section class="slide" style="left:613px;top:813px">
  <div class="abs" style="left:361px;top:232px;width:180px;height:72px;background:var(--black)"></div>
  <div class="photo" role="img" aria-label="Chef seasoning a fresh pizza on a wooden counter" style="left:285px;top:-15px;width:265px;height:265px;background:radial-gradient(circle at 45% 70%,#e8c48a,#c9a06a 45%,#b89b7a 70%,#8c7a66)"></div>
  <svg class="stroke" viewBox="0 0 541 304"><path d="M300 60 C290 150 330 220 400 240" fill="none" stroke="#fff" stroke-width="2.5" stroke-linecap="round"/></svg>
  <div class="brand light" style="left:428px;top:28px">Marlowe's</div>
  <h2 class="heading" style="left:45px;top:26px">The Market Opportunity</h2>
  <div class="rule" style="left:43px;top:60px"></div>
  <div class="sub" style="left:45px;top:82px">Overview of the<br>Pizza Industry:</div>
  <div class="body" style="left:45px;top:146px;width:205px">The pizza industry is a thriving and highly popular segment of the food service market. With a diverse range of customers and a growing demand for convenient dining options, the pizza industry presents significant growth opportunities.</div>
  <div class="footer-url">www.marlowesstonehearth.com</div>
  <div class="follow">Follow Us <i></i><i></i></div>
  <div class="page">- 4</div>
</section>

<!-- Market size -->
<section class="slide" style="left:34px;top:1057px">
  <div class="abs" role="img" aria-label="Guests sharing pizza slices at a restaurant table" style="left:352px;top:0;width:189px;height:145px;background:linear-gradient(160deg,#3a4a2e,#6b5a44 50%,#d8cfc4)"></div>
  <div class="photo" role="img" aria-label="Pepperoni pizza lifted on a peel in the kitchen" style="left:205px;top:115px;width:430px;height:430px;background:radial-gradient(circle at 40% 25%,#e9a64a,#cf7a2a 25%,#8a6a4e 45%,#4a3a30)"></div>
  <svg class="stroke" viewBox="0 0 541 304"><path d="M260 170 C330 110 440 120 500 190" fill="none" stroke="#fff" stroke-width="2.5" stroke-linecap="round"/></svg>
  <div class="brand light" style="left:425px;top:28px">Marlowe's</div>
  <h2 class="heading" style="left:45px;top:26px">The Market Opportunity</h2>
  <div class="rule" style="left:41px;top:60px"></div>
  <div class="sub" style="left:45px;top:84px">Market Size and Growth Potential:</div>
  <div class="body" style="left:45px;top:126px;width:172px">The pizza industry generates billions of dollars in revenue each year, and its potential for growth remains strong. As we expand our presence, we tap into the market's appetite for quality pizza options and capitalize on the increasing trend of takeout and delivery services.</div>
  <div class="footer-url">www.marlowesstonehearth.com</div>
</section>

<!-- Target audience -->
<section class="slide" style="left:613px;top:1300px">
  <div class="abs" style="left:0;top:253px;width:541px;height:51px;background:var(--black)"></div>
  <div class="photo" role="img" aria-label="Family of three generations enjoying pizza together" style="left:-80px;top:12px;width:276px;height:276px;background:radial-gradient(circle at 60% 45%,#d9b48e,#a8886a 40%,#6a6a72 70%,#3c3c44)"></div>
  <svg class="stroke" viewBox="0 0 541 304"><path d="M160 40 C200 110 190 200 125 270" fill="none" stroke="#fff" stroke-width="2.5" stroke-linecap="round"/></svg>
  <div class="brand light" style="left:42px;top:30px">Marlowe's</div>
  <h2 class="heading" style="left:214px;top:26px">The Market Opportunity</h2>
  <div class="rule" style="left:210px;top:62px"></div>
  <div class="sub" style="left:214px;top:82px">Target Audience and Customer<br>Demographics:</div>
  <div class="body" style="left:214px;top:158px;width:295px">Our target audience encompasses a wide range of individuals from 18 to 80 years old, both male and female, with a focus on the middle-class demographic. By offering a menu that caters to diverse tastes and preferences, we can attract a broad customer base.</div>
  <div class="follow light">Follow Us <i></i><i></i></div>
  <div class="page">- 6</div>
</section>

<!-- Unique selling proposition -->
<section class="slide" style="left:34px;top:1543px">
  <div class="photo" role="img" aria-label="Warm glow of a brick oven interior" style="left:196px;top:-49px;width:410px;height:410px;background:radial-gradient(circle at 60% 40%,#a8641e,#6e3a12 45%,#3a1e0a 80%,#1e0f06)"></div>
  <svg class="stroke" viewBox="0 0 541 304"><path d="M240 40 C190 110 190 210 260 280" fill="none" stroke="#fff" stroke-width="2.5" stroke-linecap="round"/></svg>
  <div class="brand" style="left:42px;top:30px">Marlowe's</div>
  <h2 class="heading" style="left:42px;top:90px;line-height:1.2">Unique<br>Selling<br>Proposition</h2>
  <div class="rule" style="left:37px;top:195px"></div>
  <div class="body" style="left:270px;top:45px;width:258px;font-size:8.8px;line-height:1.38;color:var(--white)">
    <p><b>What Sets Our Pizzeria Apart:</b><br>At Marlowe's Stone Hearth Pizzeria, our commitment to excellence sets us apart. We pride ourselves on using carefully crafted proprietary recipes for our homemade sauce and dough, resulting in exceptional product quality. Our small, profitable menu ensures consistency and allows us to deliver lightning-quick food times, making us a customer favorite.</p>
    <p><b>Key Differentiators and Competitive Advantages:</b><br>Our ability to make anything on our menu in a matter of minutes, coupled with our convenient ordering options, including mobile ordering, delivery service, takeout, and in-person dining, sets us apart from the competition. We prioritize meeting our customers' exact fast-paced needs and providing the best quality product and service.</p>
  </div>
  <div class="footer-url">www.marlowesstonehearth.com</div>
  <div class="page">- 7</div>
</section>

<!-- Business model -->
<section class="slide" style="left:613px;top:1787px">
  <div class="abs" role="img" aria-label="Hands shaping pizza dough balls on a floured counter" style="left:0;top:0;width:300px;height:304px;background:linear-gradient(160deg,#9a9a9a,#d6d3ce 35%,#ece8e2 65%,#e2dbd0)"></div>
  <div class="photo" style="left:225px;top:-84px;width:470px;height:470px;background:var(--black)"></div>
  <div class="icon-disc" role="img" aria-label="Laptop with sales charts" style="left:217px;top:24px;width:60px;height:60px;background:radial-gradient(#e8eef4,#9aa6b2)"></div>
  <div class="icon-disc" role="img" aria-label="Analysis dashboard on a screen" style="left:202px;top:118px;width:64px;height:64px;background:radial-gradient(#5a6470,#2a3038)"><span>Analysis</span></div>
  <div class="icon-disc" role="img" aria-label="Chalkboard welcome sign" style="left:217px;top:215px;width:60px;height:60px;background:radial-gradient(#4a4a4a,#2a2622)"></div>
  <div class="brand" style="left:41px;top:38px">Marlowe's</div>
  <h2 class="heading" style="left:41px;top:128px">Business<br>Model</h2>
  <div class="rule" style="left:37px;top:194px"></div>
  <div class="bm-text" style="top:28px"><h4>Revenue Streams:</h4>Our revenue streams include dine-in, takeout, delivery, and catering services. By offering multiple avenues for customers to enjoy our pizzas, we maximize revenue opportunities and cater to various preferences.</div>
  <div class="bm-text" style="top:114px"><h4>Pricing Strategy and Menu Overview:</h4>We have meticulously priced our menu to ensure maximum profitability while delivering value to our customers. Our menu offers a carefully selected range of signature pies, including the Hearth, Ember, and Classic pies, ensuring that each pizza is a delightful experience for our customers</div>
  <div class="bm-text" style="top:211px"><h4>Operating Hours and Location(s):</h4>Our pizzeria operates from 11 am to 9 pm, allowing us to cater to lunch and dinner crowds. Our flagship location is situated at 212 Fennel Street, Building 2, Unit 7, Easton, MD 21601, providing a convenient and accessible location for customers.</div>
  <div class="footer-url">www.marlowesstonehearth.com</div>
  <div class="page">- 8</div>
</section>

</body>
</html>
```